We need visit card and a letter paper for our website. thx

We have a beauty clinic in Switzerland.
https://wolkenbachtal.ch
We need a visit card.

Requirements
Must have
• see colors on website

```html
<!DOCTYPE html>
<html lang="de">
<head>
<meta charset="utf-8">
<title>Wolkenbachtal – Visitenkarte</title>
<link rel="stylesheet" href="https://fonts.googleapis.com/css2?family=Lato:wght@300;400&family=Roboto:wght@700&display=swap">
<style>
  :root {
    --backdrop: #d3d9d9;
    --paper: #eceae6;
    --ink: #111111;
    --ink-soft: #555555;
    --rule: #2a2a2a;
  }
  * { box-sizing: border-box; margin: 0; padding: 0; }
  html, body { width: 1200px; height: 881px; overflow: hidden; }
  body {
    background: var(--backdrop);
    display: flex;
    align-items: center;
    justify-content: center;
    gap: 60px;
    font-family: "Lato", sans-serif;
  }
  .card {
    position: relative;
    width: 500px;
    height: 300px;
    background: var(--paper);
    box-shadow: 0 8px 24px rgba(0,0,0,0.12);
  }
  .card__frame {
    position: absolute;
    inset: 14px;
    border: 1px solid var(--rule);
  }
  /* Contact side */
  .card--contact .people {
    position: absolute;
    right: 262px;
    top: 92px;
    text-align: right;
    font-family: "Roboto", sans-serif;
    font-weight: 700;
    font-size: 15px;
    line-height: 1.3;
    color: var(--ink);
  }
  .card--contact .divider {
    position: absolute;
    left: 250px;
    top: 112px;
    width: 1px;
    height: 86px;
    background: var(--rule);
  }
  .card--contact .details {
    position: absolute;
    left: 268px;
    top: 108px;
    font-size: 13px;
    font-weight: 300;
    line-height: 1.45;
    color: var(--ink-soft);
    list-style: none;
  }
  .details .address { margin-bottom: 2px; }
  .details li { display: flex; align-items: center; gap: 8px; }
  .details svg { width: 10px; height: 10px; flex: none; }
  .details .address-line { padding-left: 0; }
  /* Brand side */
  .card--brand .brand {
    position: absolute;
    inset: 0;
    display: flex;
    align-items: center;
    justify-content: center;
    font-family: "Lato", sans-serif;
    font-weight: 400;
    font-size: 40px;
    color: var(--ink);
    letter-spacing: 0.5px;
  }
</style>
</head>
<body>
  <section class="card card--contact">
    <div class="card__frame"></div>
    <div class="people">
      <p>Dr. Lena Aebischer</p>
      <p>Dr. Marco Steiner, DESA</p>
    </div>
    <div class="divider"></div>
    <ul class="details">
      <li class="address">Bachgasse 12, 7560<br>Wolkenbach, Switzerland</li>
      <li>
        <svg viewBox="0 0 10 10" aria-hidden="true"><path d="M2 1 L3.5 1 L4.2 3 L3.2 3.8 Q4 5.8 6.2 6.8 L7 5.8 L9 6.5 L9 8 Q8.5 9 7.5 9 Q2.5 8 1 2.5 Q1 1.5 2 1 Z" fill="#333"/></svg>
        +41 (0) 800 22 30 40
      </li>
      <li>
        <svg viewBox="0 0 10 10" aria-hidden="true"><rect x="0.7" y="2" width="8.6" height="6" fill="none" stroke="#333" stroke-width="0.9"/><path d="M0.7 2 L5 5.5 L9.3 2" fill="none" stroke="#333" stroke-width="0.9"/></svg>
        hallo@wolkenbachtal.ch
      </li>
      <li>
        <svg viewBox="0 0 10 10" aria-hidden="true"><circle cx="5" cy="5" r="4.3" fill="#333"/><path d="M0.7 5 H9.3 M5 0.7 V9.3 M2 2.5 H8 M2 7.5 H8" stroke="#eceae6" stroke-width="0.6" fill="none"/></svg>
        wolkenbachtal.ch
      </li>
    </ul>
  </section>

  <section class="card card--brand">
    <div class="card__frame"></div>
    <div class="brand">Wolkenbachtal</div>
  </section>
</body>
</html>
```